Aged Care Consultancy Business needs a business card design

I need a two sided business card - I want it clean and professional. Surprise me

Target Market(s)

middle aged and ageing victorians

Industry/Entity Type

Health Care

Contact Information for Business Card

Text to be included

Logo
Aged Care Consulting Services
Professional, Reliable, Affordable

Tovan Brelsick
Director
0427 31 64 92 (larger)
1300 73 29 41
tovan@wadolire.com.au
www.wadolcare.com.au
Facebook (details TBA)

include little icons beside the contact info:

- Envelope = email
- Phone = phone
- Globe = website

Font styles to use
Serif
Sans Serif

Requirements
Must have
• look proffesional and clean

```html
<!DOCTYPE html>
<html lang="en">
<head>
<meta charset="utf-8">
<title>Wadol Care – Business Card</title>
<link rel="stylesheet" href="https://fonts.googleapis.com/css2?family=Montserrat:wght@400;500;700;800&display=swap">
<style>
  :root {
    --stage: #2b2b2d;
    --card-black: #050505;
    --brand-blue: #174a8b;
    --brand-orange: #f0982a;
    --text-white: #ffffff;
  }
  * { box-sizing: border-box; margin: 0; padding: 0; }
  html, body { width: 1200px; height: 900px; overflow: hidden; }
  body {
    background: var(--stage);
    font-family: "Montserrat", Arial, sans-serif;
    display: flex; flex-direction: column; align-items: center; justify-content: center;
    gap: 40px;
  }
  .card {
    position: relative;
    width: 700px; height: 400px;
    border-radius: 26px;
    background: var(--card-black);
    overflow: hidden;
    color: var(--text-white);
  }
  /* front */
  .front-brand {
    position: absolute; left: 0; right: 0; top: 120px;
    display: flex; align-items: center; justify-content: center; gap: 18px;
  }
  .brand-dot { width: 34px; height: 34px; border-radius: 50%; background: var(--brand-blue); }
  .front-brand .brand-name { font-size: 74px; font-weight: 800; color: var(--brand-blue); letter-spacing: -1px; }
  .front-web { position: absolute; left: 0; right: 0; top: 300px; text-align: center; font-size: 24px; }
  .accent { color: var(--brand-orange); font-weight: 700; }
  /* back */
  .back-shape { position: absolute; inset: 0; }
  .back-brand {
    position: absolute; right: 50px; top: 46px;
    font-size: 58px; font-weight: 800; color: var(--brand-orange); letter-spacing: -1px;
  }
  .back-social {
    position: absolute; right: 50px; top: 130px;
    display: flex; align-items: center; gap: 10px; font-size: 18px;
  }
  .social-dot { width: 12px; height: 12px; border-radius: 50%; background: var(--brand-orange); }
  .contact-block { position: absolute; left: 42px; top: 236px; }
  .person-name { font-size: 24px; line-height: 30px; font-weight: 700; }
  .person-role { font-size: 16px; line-height: 20px; color: var(--brand-orange); margin: 0 0 8px; }
  .contact-list { list-style: none; font-size: 16px; line-height: 24px; }
  .contact-list li { display: flex; align-items: center; gap: 12px; }
  .contact-list svg { width: 14px; height: 14px; fill: none; stroke: var(--brand-orange); stroke-width: 2; flex: none; }
</style>
</head>
<body>
  <section class="card card-front">
    <div class="front-brand">
      <span class="brand-dot"></span>
      <span class="brand-name">wadol care</span>
    </div>
    <p class="front-web">www.<span class="accent">wadolcare</span>.com.au</p>
  </section>

  <section class="card card-back">
    <svg class="back-shape" viewBox="0 0 700 400" preserveAspectRatio="none" aria-hidden="true">
      <path d="M80,216 C330,206 590,170 700,70 L700,130 C560,200 300,218 0,224 Z" fill="var(--brand-orange)"/>
      <path d="M0,224 C300,218 560,200 700,112 L700,400 L0,400 Z" fill="var(--brand-blue)"/>
    </svg>
    <div class="back-brand">wadol care</div>
    <div class="back-social"><span>Social /TBA.page</span><span class="social-dot"></span></div>
    <div class="contact-block">
      <h1 class="person-name">Tovan Brelsick</h1>
      <p class="person-role">Director</p>
      <ul class="contact-list">
        <li><svg viewBox="0 0 16 16"><path d="M3 2l3 1 1 3-2 1.5a9 9 0 0 0 3.5 3.5L10 9l3 1 1 3-2 1.5C7 14 2 9 1.5 4z"/></svg>0427 31 64 92 (larger)</li>
        <li><svg viewBox="0 0 16 16"><rect x="4" y="1.5" width="8" height="13" rx="1.5"/><path d="M7 12h2"/></svg>1300 73 29 41</li>
        <li><svg viewBox="0 0 16 16"><rect x="1.5" y="3.5" width="13" height="9"/><path d="M1.5 3.5L8 9l6.5-5.5"/></svg>tovan@wadolire.com.au</li>
        <li><svg viewBox="0 0 16 16"><circle cx="8" cy="8" r="6.5"/><path d="M1.5 8h13M8 1.5c-3 3.5-3 9.5 0 13M8 1.5c3 3.5 3 9.5 0 13"/></svg>www.<span class="accent">wadolcare</span>.com.au</li>
      </ul>
    </div>
  </section>
</body>
</html>
```